Business Card Design

Just looking for a good designs that looks good with our company logo. I'd like it to be simple and to the point. Just including contact information, our logo, and my name somewhere on the card so future clients know who they're contacting, and a couple services offered. The two images I attached are pictures of our logo. I don't care which color they they are, I just attached both images to give a reference of logo colors depending on the color of the card.
Names: Calvin Prewitt
Phone: 555-247-9061
Email: tidyturfcrew@mailvista.net
Services offered:
Mowing
Fertilization
Aeration
Bed & tree maintenance
and more.
Industry/Entity Type
Business
Contact Information for Business Card
Names: Calvin Prewitt
Phone: 555-247-9061
Look and feel

```html
<!DOCTYPE html>
<html lang="en">
<head>
<meta charset="utf-8">
<title>Tidy Turf Crew – Business Card</title>
<link href="https://fonts.googleapis.com/css2?family=Signika:wght@400;600;700&display=swap" rel="stylesheet">
<style>
  :root {
    --page-bg: #e4e4e4;
    --card-bg: #f2f1ef;
    --slate: #3c3e4d;
    --coral: #e2654f;
    --coral-light: #ea7c68;
    --white: #ffffff;
  }
  * { margin: 0; padding: 0; box-sizing: border-box; }
  html, body {
    width: 1200px;
    height: 562px;
    overflow: hidden;
    background: var(--page-bg);
    font-family: "Signika", sans-serif;
  }
  .card {
    position: absolute;
    left: 150px;
    top: 24px;
    width: 900px;
    height: 514px;
    background: var(--card-bg);
    overflow: hidden;
    box-shadow: 0 6px 18px rgba(0,0,0,0.12);
  }
  .top-band {
    position: absolute;
    left: 0; right: 0;
    top: 130px;
    height: 42px;
    background: var(--slate);
  }
  .tagline {
    position: absolute;
    right: 32px;
    top: 134px;
    color: var(--coral);
    font-weight: 700;
    font-size: 27px;
    line-height: 34px;
    letter-spacing: 0.3px;
  }
  .main-panel {
    position: absolute;
    left: 0; right: 0;
    top: 180px;
    height: 240px;
    background: linear-gradient(100deg, var(--coral) 0%, var(--coral-light) 100%);
  }
  .bottom-band {
    position: absolute;
    left: 0; right: 0;
    top: 430px;
    height: 30px;
    background: var(--slate);
  }
  .brand {
    position: absolute;
    left: 92px;
    top: 74px;
    width: 136px;
    height: 136px;
    border-radius: 50%;
    background: var(--white);
    border: 4px solid var(--coral);
    display: flex;
    align-items: center;
    justify-content: center;
    text-align: center;
  }
  .brand-name {
    color: var(--slate);
    font-weight: 700;
    font-size: 22px;
    line-height: 24px;
    letter-spacing: 1px;
  }
  .person-name {
    position: absolute;
    left: 48px;
    top: 232px;
    color: var(--white);
    font-weight: 700;
    font-size: 40px;
    line-height: 48px;
  }
  .contact-list {
    position: absolute;
    left: 48px;
    top: 298px;
    list-style: none;
  }
  .contact-item {
    display: flex;
    align-items: center;
    gap: 12px;
    color: var(--white);
    font-size: 22px;
    font-weight: 600;
    height: 40px;
  }
  .contact-icon { width: 28px; height: 22px; }
  .services {
    position: absolute;
    right: 80px;
    top: 198px;
    list-style: none;
    text-align: right;
    color: var(--white);
    font-weight: 700;
    font-size: 22px;
    line-height: 29px;
  }
  .mower-illustration {
    position: absolute;
    left: 440px;
    top: 352px;
    width: 300px;
    height: 68px;
    border-radius: 34px 34px 0 0;
    background: linear-gradient(180deg, rgba(255,255,255,0.55), rgba(255,255,255,0.35));
  }
</style>
</head>
<body>
  <div class="card">
    <div class="top-band"></div>
    <p class="tagline">Quality Guaranteed</p>
    <div class="main-panel"></div>
    <div class="bottom-band"></div>
    <div class="mower-illustration" role="img" aria-label="Illustration of a push lawn mower with grass tufts and garden shears"></div>

    <div class="brand">
      <span class="brand-name">TIDY<br>TURF<br>CREW</span>
    </div>

    <h1 class="person-name">Calvin Prewitt</h1>
    <ul class="contact-list">
      <li class="contact-item">
        <svg class="contact-icon" viewBox="0 0 28 22" aria-hidden="true">
          <path d="M2 7 Q14 -1 26 7 L23 10 L19 8 L19 5 Q14 3 9 5 L9 8 L5 10 Z" fill="#3c3e4d"/>
          <path d="M7 11 L21 11 L25 20 L3 20 Z" fill="#3c3e4d"/>
          <circle cx="14" cy="15.5" r="2.6" fill="#e2654f"/>
        </svg>
        <span>555-247-9061</span>
      </li>
      <li class="contact-item">
        <svg class="contact-icon" viewBox="0 0 28 22" aria-hidden="true">
          <rect x="1" y="2" width="26" height="18" rx="2" fill="#3c3e4d"/>
          <path d="M2 4 L14 13 L26 4" fill="none" stroke="#e2654f" stroke-width="2"/>
        </svg>
        <span>tidyturfcrew@mailvista.net</span>
      </li>
    </ul>

    <ul class="services">
      <li>Mowing</li>
      <li>Fertilization</li>
      <li>Aeration</li>
      <li>Bed &amp; tree maintenance</li>
      <li>and more.</li>
    </ul>
  </div>
</body>
</html>
```